*** Business Card Design Project

I need a logo and business card for my new catering business: "Brevano". The design should be modern, clean, elegant and refined. One or Two colours only. The design SHOULD NOT include graphics or images. There should be space for my name, phone number and email address (I will provide these to you later).

Industry/Entity Type

Catering

Requirements
Must have
• Must have one or two colours only.
Must include the text "brevano"
Should not have
• Must not have graphics or images.

```html
<!DOCTYPE html>
<html lang="en">
<head>
<meta charset="utf-8">
<title>Brevano Catering – Business Card</title>
<link rel="stylesheet" href="https://fonts.googleapis.com/css2?family=Marcellus+SC&display=swap">
<style>
  :root {
    --backdrop: #eeefe2;
    --paper: #ffffff;
    --lime: #bcd64d;
    --cocoa: #452b1d;
    --cream-text: #ffffff;
    --card-font: "Marcellus SC", serif;
  }
  * { margin: 0; padding: 0; box-sizing: border-box; }
  html, body {
    width: 1200px;
    height: 900px;
    overflow: hidden;
    background: var(--backdrop);
    font-family: var(--card-font);
  }
  .business-card {
    position: absolute;
    left: 146px;
    top: 158px;
    width: 907px;
    height: 560px;
    background: var(--paper);
    overflow: hidden;
  }
  .brand-panel {
    position: absolute;
    left: 0; top: 0;
    width: 100%;
    height: 213px;
    background: var(--paper);
    border-bottom: 6px solid var(--cocoa);
    display: flex;
    align-items: center;
    justify-content: center;
    gap: 16px;
  }
  .brand-dot {
    width: 18px;
    height: 18px;
    border-radius: 50%;
    background: var(--lime);
    flex: none;
  }
  .brand-name {
    font-size: 40px;
    line-height: 1;
    letter-spacing: 0.02em;
    font-weight: 400;
    color: var(--cocoa);
  }
  .identity-band {
    position: absolute;
    left: 0; top: 219px;
    width: 100%;
    height: 115px;
    background: var(--lime);
    border-bottom: 6px solid var(--paper);
    text-align: center;
    color: var(--cocoa);
  }
  .person-name {
    position: absolute;
    left: 0; right: 0;
    top: 27px;
    font-size: 36px;
    letter-spacing: 0.06em;
    line-height: 1;
    font-weight: 400;
  }
  .person-role {
    position: absolute;
    left: 0; right: 0;
    top: 70px;
    font-size: 20px;
    letter-spacing: 0.2em;
    padding-left: 0.2em;
    line-height: 1;
    text-transform: lowercase;
  }
  .contact-panel {
    position: absolute;
    left: 0; top: 340px;
    width: 100%;
    height: 220px;
    background: var(--cocoa);
    color: var(--cream-text);
  }
  .contact-list {
    list-style: none;
    position: absolute;
    left: 79px;
    top: 38px;
    font-size: 19px;
    letter-spacing: 0.1em;
    line-height: 38.5px;
    text-transform: uppercase;
    white-space: nowrap;
  }
  .contact-label { margin-right: 0.4em; }
</style>
</head>
<body>
  <article class="business-card">
    <header class="brand-panel">
      <span class="brand-dot" aria-hidden="true"></span>
      <h1 class="brand-name">Brevano Catering</h1>
    </header>
    <section class="identity-band">
      <h2 class="person-name">Ravi Mendhan</h2>
      <p class="person-role">Owner</p>
    </section>
    <footer class="contact-panel">
      <ul class="contact-list">
        <li><span class="contact-label">T:</span>0770 900 4127</li>
        <li><span class="contact-label">E:</span>brevanocaters@inboxmail.net</li>
        <li><span class="contact-label">W:</span>www.brevanocatering.co.uk</li>
      </ul>
    </footer>
  </article>
</body>
</html>
```